Corvana Wound Care Business card design

We need a business card designed around our logo which was provided. The logo of preference is the colored. Also the colors and fonts were provided.

Target Market(s)

Our Referral partners are home health agencies.

Industry/Entity Type

Healthcare

Contact Information for Business Card

Name , Phone #, Email , Title

Requirements
Nice to have
• Creativity
Should not have
• basic

```html
<!DOCTYPE html>
<html lang="en">
<head>
<meta charset="utf-8">
<title>Corvana Wound Care – Business Card</title>
<link rel="stylesheet" href="https://fonts.googleapis.com/css2?family=Poppins:wght@400;500;600;700&display=swap">
<style>
  :root {
    --bg: #2b2c2f;
    --card-white: #ffffff;
    --brand-navy: #024b91;
    --brand-blue: #0a5cb8;
    --brand-sky: #1ea0e6;
    --ink: #2a2a2a;
    --muted: #3a3a3a;
    --back-text: #2f73c4;
  }
  * { box-sizing: border-box; margin: 0; padding: 0; }
  html, body { width: 1200px; height: 794px; overflow: hidden; }
  body {
    background: var(--bg);
    font-family: "Poppins", sans-serif;
    position: relative;
  }
  .card {
    position: absolute;
    width: 500px;
    height: 286px;
    border-radius: 22px;
    overflow: hidden;
  }

  /* Back side */
  .card-back {
    left: 60px;
    top: 254px;
    background: var(--brand-navy);
    display: flex;
    align-items: center;
    justify-content: center;
  }
  .back-brand {
    color: var(--back-text);
    font-weight: 500;
    text-align: center;
    line-height: 1;
  }
  .back-brand .brand-main { display: block; font-size: 58px; letter-spacing: 1px; }
  .back-brand .brand-sub { display: block; font-size: 13px; letter-spacing: 14px; margin-top: 12px; padding-left: 14px; text-transform: uppercase; }

  /* Front side */
  .card-front {
    left: 640px;
    top: 254px;
    background: var(--card-white);
  }
  .front-brand {
    position: absolute;
    right: 36px;
    top: 58px;
    display: flex;
    align-items: center;
    gap: 10px;
  }
  .front-brand .brand-dot {
    width: 16px; height: 16px; border-radius: 50%;
    background: var(--brand-blue);
  }
  .front-brand .brand-name {
    font-size: 22px;
    font-weight: 600;
    color: var(--brand-navy);
    line-height: 1;
  }
  .holder {
    position: absolute;
    left: 34px;
    top: 108px;
  }
  .holder-name {
    font-size: 21px;
    font-weight: 600;
    color: var(--ink);
    text-transform: uppercase;
    letter-spacing: 0.3px;
    line-height: 1.1;
  }
  .holder-title {
    font-size: 14px;
    font-weight: 500;
    color: var(--brand-blue);
    margin-top: 2px;
  }
  .divider {
    position: absolute;
    left: 34px;
    top: 166px;
    width: 428px;
    height: 1.5px;
    background: linear-gradient(90deg, var(--brand-blue), var(--brand-sky));
  }
  .contacts {
    position: absolute;
    left: 34px;
    top: 176px;
    list-style: none;
    font-size: 10.5px;
    color: var(--muted);
    line-height: 1.75;
  }
  .contacts li { display: flex; align-items: center; gap: 6px; }
  .contacts svg { width: 11px; height: 11px; flex: none; }
  .address {
    position: absolute;
    right: 38px;
    top: 176px;
    font-size: 10.5px;
    font-style: normal;
    color: var(--muted);
    text-align: right;
    line-height: 1.75;
  }
  .front-band {
    position: absolute;
    left: 0; bottom: 0;
    width: 500px; height: 26px;
  }
</style>
</head>
<body>
  <section class="card card-back" aria-label="Card back">
    <div class="back-brand">
      <span class="brand-main">Corvana</span>
      <span class="brand-sub">Wound Care</span>
    </div>
  </section>

  <section class="card card-front" aria-label="Card front">
    <div class="front-brand">
      <span class="brand-dot"></span>
      <span class="brand-name">Corvana Wound Care</span>
    </div>

    <div class="holder">
      <h1 class="holder-name">Dana Whitford</h1>
      <p class="holder-title">senior consultant</p>
    </div>

    <div class="divider"></div>

    <ul class="contacts">
      <li>
        <svg viewBox="0 0 12 12"><rect width="12" height="12" rx="2" fill="#0a5cb8"/><path d="M4 3.2l1 1.6-.7.7c.5 1 1.2 1.7 2.2 2.2l.7-.7 1.6 1-.5 1.1C6 9 3 6 2.9 3.7z" fill="#fff"/></svg>
        +1 (555) 214-7730
      </li>
      <li>
        <svg viewBox="0 0 12 12"><rect width="12" height="12" rx="2" fill="#0a5cb8"/><rect x="2.5" y="3.5" width="7" height="5" rx=".6" fill="none" stroke="#fff" stroke-width=".9"/><path d="M2.7 3.8L6 6.4l3.3-2.6" fill="none" stroke="#fff" stroke-width=".9"/></svg>
        dana.whitford@corvana.com
      </li>
    </ul>

    <address class="address">
      418 Larkfield Ave #210<br>
      Bellmont, Texas(TX), 78540
    </address>

    <svg class="front-band" viewBox="0 0 500 26" preserveAspectRatio="none" aria-hidden="true">
      <defs>
        <linearGradient id="bandFade" x1="0" x2="1" y1="0" y2="0">
          <stop offset="0" stop-color="#0a5cb8"/>
          <stop offset="1" stop-color="#1ea0e6"/>
        </linearGradient>
      </defs>
      <rect x="0" y="18" width="240" height="8" fill="url(#bandFade)"/>
      <path d="M236 26 L236 14 Q236 6 246 6 L500 6 L500 26 Z" fill="#024b91"/>
    </svg>
  </section>
</body>
</html>
```